Marlow Yardcraft need a flyer - A6 - Double sided

We need a flyer that will engage potential customer in need for gardening services. We offer high quality gardening services spanning from lawn mowing and weeding to soil improvement to tree pruning and so on.
I would like a double sided flyer A6 size. I trust your expert touch in terms of lay out but the general idea I had was to have one side with the logo, a catchy picture (or more), the website/phone number/address and on the flip side a little more text focusing on the client perspective with statement such as 'Let us do the hard work so that you can enjoy your garden' (obviously the wording isn't my strongest skill) but the idea is to get into the customer perspective;
I would also like to list all the service we can offer such as but not limited to weeding, pruning, lawn care, green waste disposal, soil improvement, hedging, edging, lawn mowing,...
Happy for you to use any picture free of right from the internet if necessary

Target Market(s)

Home owner & Businesses

Industry/Entity Type

Landscape Gardening

Requirements
Must have
• website - http://yardcraft-marlow.com.au (feel free to browse the website to get ideas on color theme and overall look)
• phone number - (08) 6341 2705
Nice to have
• a list of services on offer
• phone number and website
• being customer perspective focused (the benefits for the customer) - perhaps on the flip side some text like 'highly trained and experienced landscape gardeners so that the job is done perfectly every time', 'always carrying all range of commercial grade tools so that we can tackle any job', 'Experienced gardeners so that the job is achieve faster' (it doesn't have to be in those exact words as I trust that you may be expert in wording as well as designers?)

```html
<!DOCTYPE html>
<html lang="en">
<head>
<meta charset="utf-8">
<title>Marlow Yardcraft – A6 Flyer</title>
<link href="https://fonts.googleapis.com/css2?family=Mulish:wght@400;600;700;800&display=swap" rel="stylesheet">
<style>
:root{
  --backdrop:#dcd9da;
  --paper:#ffffff;
  --ink:#2b2b2b;
  --green-dark:#2f6f1f;
  --green:#4ab51f;
  --green-mid:#8fcc45;
  --green-light:#c3ef79;
  --lawn:#6fa534;
  --orange:#e8662a;
}
*{box-sizing:border-box;margin:0;padding:0}
html,body{width:1200px;height:900px;overflow:hidden}
body{background:var(--backdrop);font-family:"Mulish",sans-serif;color:var(--ink);position:relative}
.flyer{position:absolute;top:134px;height:631px;background:var(--paper);overflow:hidden;box-shadow:3px 4px 8px rgba(0,0,0,.35)}
.flyer--front{left:120px;width:448px}
.flyer--back{left:632px;width:442px}
.photo{position:absolute}
.green-band{position:absolute;left:0;right:0;bottom:0;background:linear-gradient(100deg,#7cc23a 0%,#a6dc5a 45%,#c8f57f 65%,#9ed650 100%)}

/* front */
.hero{left:0;top:0;width:448px;height:271px;background:linear-gradient(170deg,#7a9a4c 0%,#5f9a2c 40%,#7fb93a 70%,#4d8a22 100%)}
.brand{position:absolute;left:33px;top:99px;width:135px;height:64px;background:#fff;border-radius:8px;display:flex;align-items:center;justify-content:center;text-align:center;font-weight:800;font-size:19px;line-height:1.05;color:var(--green-dark)}
.about{position:absolute;left:0;top:271px;width:448px;height:120px}
.offer{position:absolute;left:26px;top:216px;width:124px;height:124px;border-radius:50%;background:#fff;border:7px solid var(--green);box-shadow:0 0 0 3px #fff;text-align:center;padding-top:16px;color:var(--ink)}
.offer__num{font-size:30px;font-weight:600;line-height:1}
.offer__num small{font-size:17px}
.offer__text{font-size:15px;line-height:1.1}
.offer__text b{font-size:19px;font-weight:600;display:block}
.call{position:absolute;left:30px;top:344px;width:120px;text-align:center}
.call__label{font-size:19px;font-weight:600}
.call__phone{font-size:16px;font-weight:800;color:var(--green-dark);margin-top:2px;white-space:nowrap;margin-left:-6px}
.about__title{position:absolute;left:170px;top:284px;font-size:18px;font-weight:600}
.about__text{position:absolute;left:170px;top:310px;width:255px;font-size:11.3px;line-height:1.35}
.strip{top:391px;height:102px}
.strip--garden{left:0;width:148px;background:linear-gradient(160deg,#6f9f4a,#c65aa0 55%,#e2c23c)}
.strip--beet{left:148px;width:150px;background:radial-gradient(circle at 45% 65%,#8a1b2c,#5e1420 60%,#6d8f3b)}
.strip--border{left:298px;width:150px;background:linear-gradient(160deg,#5f8f3e,#86b35a 50%,#d9465b)}
.hours{position:absolute;left:0;top:493px;width:448px;height:16px;text-align:center;font-size:11.5px;line-height:16px}
.flyer--front .green-band{height:122px}
.swoosh{position:absolute;left:0;top:0}
.services{position:absolute;left:53px;top:10px}
.services__title{font-size:17px;font-weight:600;color:#1f3f12}
.services__cols{display:flex;gap:26px;margin-top:2px}
.services ul{list-style:none;font-size:11.5px;line-height:18.5px}
.services li::before{content:"✓";margin-right:4px;font-size:10px}

/* back */
.garden{left:0;top:0;width:442px;height:218px;background:linear-gradient(135deg,#5f8a3a 0%,#b8c08a 35%,#e4c53e 60%,#cf5aa0 85%,#7ea94a 100%)}
.crew{left:0;top:218px;width:442px;height:126px;background:linear-gradient(90deg,#3d5a2e 0%,#6a8f44 35%,#7aa24b 65%,#4c6d33 100%)}
.award{position:absolute;left:154px;top:218px;width:120px;height:120px;border-radius:50%;background:var(--green-mid);padding:10px}
.award span{display:block;width:100%;height:100%;border-radius:50%;background:var(--orange)}
.tagline{position:absolute;left:0;top:356px;width:442px;text-align:center;font-size:16px;line-height:21px}
.benefits{position:absolute;left:31px;top:414px;width:400px}
.benefits__title{font-size:15px;font-weight:800}
.benefits ul{list-style:none;margin-top:4px;font-size:11.3px;line-height:15px}
.benefits li{position:relative;padding-left:10px;margin-bottom:1px}
.benefits li::before{content:"";position:absolute;left:0;top:6px;width:4px;height:4px;border-radius:50%;background:var(--green)}
.flyer--back .green-band{height:108px}
.contact{position:absolute;left:31px;top:10px;font-size:12px;line-height:15px}
.contact__title{font-size:15px;font-weight:800;margin-bottom:4px}
.contact__row{display:flex;align-items:flex-start;gap:5px}
.contact__row svg{flex:none;margin-top:2px}
.contact__indent{padding-left:14px}
</style>
</head>
<body>

<section class="flyer flyer--front">
  <div class="photo hero" role="img" aria-label="Close-up of a red lawn mower on freshly cut green grass with flower beds behind"></div>
  <div class="brand">Marlow<br>Yardcraft</div>
  <div class="about"></div>
  <div class="offer">
    <div class="offer__num">00<small>%</small></div>
    <div class="offer__text">services on<b>offer</b></div>
  </div>
  <div class="call">
    <div class="call__label">Call Us:</div>
    <div class="call__phone">(08) 6341 2705</div>
  </div>
  <h2 class="about__title">About Us:</h2>
  <p class="about__text">We’re proud to have built a reputation as a versatile landscape gardening company that delivers professional service and high quality results.</p>
  <div class="photo strip strip--garden" role="img" aria-label="Colourful patterned flower garden bed"></div>
  <div class="photo strip strip--beet" role="img" aria-label="Freshly harvested beetroot with leaves"></div>
  <div class="photo strip strip--border" role="img" aria-label="Landscaped garden with flowering borders"></div>
  <p class="hours">Operating hours: Monday to Friday, 8.30am - 5.30pm</p>
  <div class="green-band">
    <svg class="swoosh" width="448" height="122" viewBox="0 0 448 122" aria-hidden="true">
      <path d="M0 122 C60 70 150 30 320 22 L448 18 L448 0 C300 10 140 20 0 90 Z" fill="#ffffff" opacity=".18"/>
      <path d="M0 60 C40 40 90 28 150 24 C90 40 40 70 20 122 L0 122 Z" fill="#5aa82a" opacity=".35"/>
    </svg>
    <div class="services">
      <h3 class="services__title">Our Services:</h3>
      <div class="services__cols">
        <ul>
          <li>Lawn Care</li>
          <li>Tree pruning &amp; Plant Care</li>
          <li>Hedge trimming</li>
          <li>Organic Gardening</li>
        </ul>
        <ul style="margin-top:-18px">
          <li>Mulching</li>
          <li>Weed Control</li>
          <li>Rubbish &amp; Green Waste Removal</li>
          <li>Fertilising &amp; Soil Improvement</li>
        </ul>
      </div>
    </div>
  </div>
</section>

<section class="flyer flyer--back">
  <div class="photo garden" role="img" aria-label="Watering can and straw hat among yellow and pink garden flowers"></div>
  <div class="photo crew" role="img" aria-label="Two gardeners at work among shrubs and trees"></div>
  <div class="award" aria-label="Service award badge"><span></span></div>
  <p class="tagline">Let us do the hard work<br>so that you can enjoy your garden</p>
  <div class="benefits">
    <h3 class="benefits__title">Benefits for the customer:</h3>
    <ul>
      <li>Highly trained and experienced landscape gardeners so that the job is done perfectly every time</li>
      <li>Always carrying all range of commercial grade tools so that we can tackle any job</li>
      <li>Experienced gardeners so that the job is achieve faster</li>
    </ul>
  </div>
  <div class="green-band">
    <div class="contact">
      <h3 class="contact__title">Contact Us:</h3>
      <div class="contact__row">
        <svg width="9" height="11" viewBox="0 0 9 11" aria-hidden="true"><path d="M4.5 0A4 4 0 0 0 .5 4c0 3 4 7 4 7s4-4 4-7a4 4 0 0 0-4-4zm0 5.5a1.5 1.5 0 1 1 0-3 1.5 1.5 0 0 1 0 3z" fill="#fff"/></svg>
        <span>Level 12, 40 Harbour Row</span>
      </div>
      <div class="contact__indent">Marlow, WA 6010</div>
      <div class="contact__row">
        <svg width="9" height="10" viewBox="0 0 9 10" aria-hidden="true"><path d="M2 0l2 2.5-1 1.2a6 6 0 0 0 2.4 2.6l1.1-1L9 7.2 7.6 9.5C4 9.5 0 5.5 0 1.5z" fill="#fff"/></svg>
        <span>08 6341 2790</span>
      </div>
      <div class="contact__row">
        <svg width="9" height="9" viewBox="0 0 10 10" aria-hidden="true"><circle cx="5" cy="5" r="4.5" fill="#fff"/><path d="M.5 5h9M5 .5c-2.5 3-2.5 6 0 9M5 .5c2.5 3 2.5 6 0 9" stroke="#8fcc45" stroke-width=".8" fill="none"/></svg>
        <span>yardcraft-marlow.com.au</span>
      </div>
    </div>
  </div>
</section>

</body>
</html>
```